Flyer design for mobile apps service for small/medium businesses

KelvoraPocket is a service line of KelvoraWorks Ltd, which aims to provide a bespoke mobile app building service to small and medium businesses. The focus of this business is to team closely with the small business to understand their motivation and advise them on gaining a mobile presence, first a small one, then to grow as their customers feed back their approval.I would like mainly use of the colours in the app logo (green and gold) but others could be use for emphasizing text.The final design should communicate "we are on the side of small business, want you to succeed in getting a mobile presence"The reverse side of the flyer should say something about the company and its approach to doing this, as well as include contact info and a QR code of the website (kelvorapocket.uk)The images I am providing include six of typical small businesses, one of arms holding mobile phones, one of mobile devices exploding with apps. ALso the logo for kelvorapocket, which should be prominent..

Target Market(s)

Small business owners

Industry/Entity Type

Building

Requirements
Must have
• Images of small businesses (provided)
• Logo
• Key text entries (all or some of - see attached word doc)
• The strapline for the business: "The Smarter Business Gets Mobile"
• Consistent colour scheme
• Reverse side with contact info and QR code of websirte

```html
<!DOCTYPE html>
<html lang="en">
<head>
<meta charset="utf-8">
<title>KelvoraPocket – Mobile Apps for Small Business</title>
<link rel="stylesheet" href="https://fonts.googleapis.com/css2?family=Roboto+Condensed:wght@400;500&display=swap">
<style>
  :root {
    --bg: #eef2ee;
    --gold: #f0d00c;
    --green: #1d6a22;
    --tile-gap: #ffffff;
  }
  html, body {
    margin: 0;
    padding: 0;
    width: 1200px;
    height: 851px;
    overflow: hidden;
    background: var(--bg);
  }
  .flyer {
    position: relative;
    width: 1200px;
    height: 851px;
    background: var(--bg);
    font-family: "Roboto Condensed", "Arial Narrow", sans-serif;
    overflow: hidden;
  }
  .artwork {
    position: absolute;
    inset: 0;
  }
  .brand {
    position: absolute;
    left: 632px;
    top: 26px;
    width: 222px;
    color: var(--green);
  }
  .brand__name {
    display: flex;
    align-items: center;
    gap: 8px;
    margin: 0;
    font-size: 27px;
    font-weight: 500;
    line-height: 32px;
  }
  .brand__dot {
    width: 16px;
    height: 16px;
    border-radius: 50%;
    background: var(--gold);
    flex: none;
  }
  .brand__strapline {
    margin: 6px 0 0;
    font-size: 15px;
    font-weight: 400;
    line-height: 19px;
  }
  .callout {
    position: absolute;
    display: flex;
    align-items: center;
    justify-content: center;
    text-align: center;
    color: var(--green);
    font-size: 17px;
    font-weight: 500;
    line-height: 24px;
    margin: 0;
  }
  .callout--reach   { left: 880px; top: 44px;  width: 300px; height: 106px; }
  .callout--booking { left: 585px; top: 188px; width: 350px; height: 108px; }
  .callout--cost    { left: 860px; top: 333px; width: 310px; height: 108px; }
  .callout--contact { left: 540px; top: 478px; width: 300px; height: 108px; }
  .callout--about   { left: 815px; top: 621px; width: 360px; height: 108px; }
  .callout--closing { left: 430px; top: 705px: width: 340px; height: 96px; }
  .callout--closing { left: 430px; top: 705px; width: 340px; height: 96px; }
</style>
</head>
<body>
<main class="flyer">
  <svg class="artwork" width="1200" height="851" viewBox="0 0 1200 851" xmlns="http://www.w3.org/2000/svg">
    <defs>
      <clipPath id="collage-edge">
        <path d="M0,0 H598 Q616,4 614,26 L394,822 Q388,842 370,844 L0,851 Z"/>
      </clipPath>
      <linearGradient id="g-glass" x1="0" y1="0" x2="1" y2="1">
        <stop offset="0" stop-color="#6f7d86"/><stop offset="1" stop-color="#2e3a46"/>
      </linearGradient>
      <linearGradient id="g-salon" x1="0" y1="0" x2="1" y2="1">
        <stop offset="0" stop-color="#b4aaa0"/><stop offset="1" stop-color="#3a3432"/>
      </linearGradient>
      <linearGradient id="g-florist" x1="0" y1="0" x2="1" y2="1">
        <stop offset="0" stop-color="#c7a47e"/><stop offset="1" stop-color="#6b5a7a"/>
      </linearGradient>
      <linearGradient id="g-flowers" x1="0" y1="0" x2="1" y2="1">
        <stop offset="0" stop-color="#d0526c"/><stop offset="0.5" stop-color="#4f7a3c"/><stop offset="1" stop-color="#e8e6dc"/>
      </linearGradient>
      <linearGradient id="g-bike" x1="0" y1="0" x2="1" y2="1">
        <stop offset="0" stop-color="#8a8a78"/><stop offset="1" stop-color="#2f4a34"/>
      </linearGradient>
      <linearGradient id="g-van" x1="0" y1="0" x2="1" y2="1">
        <stop offset="0" stop-color="#58b6d8"/><stop offset="0.5" stop-color="#d8dde2"/><stop offset="1" stop-color="#1f2c4a"/>
      </linearGradient>
      <linearGradient id="g-dentist" x1="0" y1="0" x2="1" y2="1">
        <stop offset="0" stop-color="#e9eef0"/><stop offset="0.6" stop-color="#e6c2ae"/><stop offset="1" stop-color="#8ec6dc"/>
      </linearGradient>
    </defs>

    <g class="collage" clip-path="url(#collage-edge)">
      <rect class="collage__gaps" x="0" y="0" width="620" height="851" fill="var(--tile-gap)"/>
      <rect role="img" aria-label="Photo: technicians fitting a car windscreen" x="0" y="0" width="249" height="163" fill="url(#g-glass)"/>
      <rect role="img" aria-label="Photo: hairdressers styling clients in a salon" x="252" y="17" width="380" height="274" fill="url(#g-salon)"/>
      <rect role="img" aria-label="Photo: florist holding a bouquet in her shop" x="0" y="166" width="250" height="261" fill="url(#g-florist)"/>
      <rect role="img" aria-label="Photo: colourful cut flowers on display" x="250" y="294" width="320" height="178" fill="url(#g-flowers)"/>
      <rect role="img" aria-label="Photo: mechanic repairing a bicycle in a workshop" x="0" y="430" width="221" height="193" fill="url(#g-bike)"/>
      <rect role="img" aria-label="Photo: two tradesmen standing by their van" x="224" y="476" width="300" height="147" fill="url(#g-van)"/>
      <rect role="img" aria-label="Photo: dentist examining a smiling patient" x="0" y="626" width="450" height="225" fill="url(#g-dentist)"/>
    </g>

    <path class="accent-band" d="M606,124 Q616,126 618,138 L410,778 Q406,788 400,792 L404,770 Z" fill="var(--gold)"/>

    <g class="callout-frames" fill="none" stroke="var(--gold)" stroke-width="3.5" stroke-linejoin="round">
      <path d="M1200,34 H902 Q894,34 890,42 L860,128 Q856,138 864,150 Q870,160 882,160 H1200"/>
      <path d="M600,177 H908 Q914,177 918,184 L968,272 Q972,280 966,292 Q960,305 948,305 H558"/>
      <path d="M1200,323 H882 Q874,323 870,331 L818,424 Q814,432 820,442 Q826,451 838,451 H1200"/>
      <path d="M504,468 H858 Q864,468 868,475 L917,560 Q922,570 916,582 Q910,596 898,596 H462"/>
      <path d="M1200,611 H820 Q812,611 808,619 L782,704 Q778,714 786,726 Q792,739 804,739 H1200"/>
      <path d="M431,689 H726 Q732,689 736,696 L789,786 Q794,796 788,806 Q782,817 770,817 H389"/>
    </g>
  </svg>

  <header class="brand">
    <p class="brand__name"><span class="brand__dot"></span>KelvoraPocket</p>
    <p class="brand__strapline">The Smarter Business Gets Mobile</p>
  </header>

  <p class="callout callout--reach">This is a great opportunity<br>to put your business on those<br>all-pervasive devices that people never<br>seem to put down!</p>
  <p class="callout callout--booking">With a mobile app for your business you can<br>make it easier for customers to book<br>appointments, access discounts,view<br>your products/services and communicate with you</p>
  <p class="callout callout--cost">It may be cheaper than you think to<br>produce a mobile app that allows your<br>customers to engage with you like<br>they never could before!</p>
  <p class="callout callout--contact">Don't disadvantage your business:<br>join the mobile world.Contact us now to<br>discuss the possibilities for a business<br>like yours (you may be surprised!)</p>
  <p class="callout callout--about">We are a small business ourselves,<br>based here in the UK (Kent), and our mission is to<br>support other local businesses by helping<br>them take advantage of the mobile world.</p>
  <p class="callout callout--closing">Whatever business you run, however small,<br>it is in your interest to explore the benefits of the<br>mobile world, so please get in touch!</p>
</main>
</body>
</html>
```